Visitenkarten-Design für Psycho-Kinesiologie Praxis
Zielgruppe
praxis für Psycho-Kinesiologie - Systematische Familienaufstellungen. Einzelsitzungen Gruppentherapie
Ich suche ein Design was auf der einen Seite auffällt, aus dem Rahmen fällt und trotzdem seriös wirkt und Vertrauen schafft.
Die Anhänge sind nur meine Entwürfe also keine fixen Vorgaben
Aufgabenstellung
Eine Seite soll auffallen und Kreativ gestaltet sein
Es gibt ein Template aber die Farben sind noch nicht definiert.
https://www.vorlagenhafen.com/de/demo/48352.html
Es gibt ein Logo (Systemanalytiker) da sind die Farben auch nicht fix Definiert. Gerne sehe ich verschiedene Farbkombinationen
Foto: besseres folgt in kürze
Lumen Harbor Circle: Kann auf einer Seite drauf sein, wenn genug Platz,

```html
<!DOCTYPE html>
<html lang="de">
<head>
<meta charset="utf-8">
<title>Visitenkarten Seelenklang – Varianten</title>
<link rel="stylesheet" href="https://fonts.googleapis.com/css2?family=Jost:wght@300;400&family=Lora:ital,wght@0,400;1,400&display=swap">
<style>
:root{
  --paper:#ffffff;
  --slate:#2a2e31;
  --slate-band:#3b3f43;
  --wine:#a11d2c;
  --wine-bright:#c8202f;
  --ink-light:#ffffff;
  --ink-soft:#d9d9d9;
  --photo-light:#b9b9b9;
  --photo-dark:#4a4a4a;
}
*{margin:0;padding:0;box-sizing:border-box}
html,body{width:857px;height:1200px;overflow:hidden;background:var(--paper)}
body{position:relative;font-family:"Jost",sans-serif;color:var(--ink-light)}
.pair{position:absolute;left:0;width:857px;height:154px}
.card{position:absolute;top:0;width:238px;height:154px;overflow:hidden;box-shadow:0 2px 4px rgba(0,0,0,.25)}
.card--front{left:181px;background:var(--slate)}
.card--back{left:444px;background:var(--wine)}
.reject-mark{position:absolute;left:138px;top:62px;color:var(--wine);font:300 24px "Jost",sans-serif}

.values-band{position:absolute;left:0;bottom:0;width:100%;height:13px;background:var(--slate-band);border-top:1.5px solid var(--wine-bright);
  display:flex;justify-content:center;gap:11px;align-items:center;font-size:7px;letter-spacing:1.6px;color:var(--ink-light)}

.crescent{position:absolute;top:0;right:0;width:238px;height:142px}

.wordmark{position:absolute;display:flex;align-items:center;gap:4px;font-weight:300;color:var(--ink-light);white-space:nowrap}
.wordmark__dot{width:7px;height:7px;border-radius:50%;background:var(--wine-bright)}
.wordmark-sub{position:absolute;font-size:6px;font-weight:300;color:var(--ink-soft)}

.front__logo{left:34px;top:58px;font-size:29px}
.front__logo .wordmark__dot{width:10px;height:10px}
.front__sub{left:154px;top:94px;font-size:6.5px}
.front__services{position:absolute;left:0;width:100%;top:108px;text-align:center;font-size:6px;line-height:8.6px;color:var(--ink-light)}
.front__name{position:absolute;left:127px;top:105px;font:italic 11.5px "Lora",serif}

.back__half{position:absolute;top:0;height:142px;width:119px}
.back__half--left{left:0}
.back__half--right{left:119px}
.photo{background:linear-gradient(200deg,var(--photo-light),#8c8c8c 45%,var(--photo-dark))}
.back__panel-dark{background:var(--slate)}

.back__logo{left:9px;top:10px;font-size:17px}
.back__logo-sub{left:74px;top:32px;font-size:4px}
.person-name{position:absolute;font:400 10px "Lora",serif}
.person-role{position:absolute;font-size:7.5px;font-weight:300}
.contact{position:absolute;left:10px;font-size:6px;line-height:8px;list-style:none}
.contact li{display:flex;gap:3px;align-items:center}
.contact li.indent{padding-left:8px}
.contact svg{width:5px;height:5px;flex:none}
.services{position:absolute;left:9px;top:14px;font-size:6px;line-height:9px;list-style:none}
.services li::before{content:"·";margin-right:2px}
.services li.cont{padding-left:4px}
.services li.cont::before{content:""}
.partner-badge{position:absolute;width:26px;height:18px;border-radius:9px;background:var(--wine-bright)}
.partner-name{position:absolute;font-size:5.5px;font-weight:400;white-space:nowrap}
</style>
</head>
<body>

<!-- reusable icon shapes -->
<svg width="0" height="0" style="position:absolute">
  <defs>
    <linearGradient id="arc-fade" x1="0" y1="0" x2="1" y2="0">
      <stop offset="0" stop-color="#a11d2c" stop-opacity="0"/>
      <stop offset=".6" stop-color="#a11d2c" stop-opacity=".8"/>
      <stop offset="1" stop-color="#c8202f"/>
    </linearGradient>
    <symbol id="icon-phone" viewBox="0 0 10 10"><path d="M2 0.5 L4 3 L3 4.2 Q4 6.4 5.8 7 L7 6 L9.5 8 L8.3 9.5 Q3 9 0.6 2 Z" fill="#fff"/></symbol>
    <symbol id="icon-mail" viewBox="0 0 10 10"><rect x="0.5" y="2" width="9" height="6" fill="#fff"/><path d="M0.5 2 L5 5.5 L9.5 2" stroke="#a11d2c" fill="none"/></symbol>
    <symbol id="icon-web" viewBox="0 0 10 10"><circle cx="5" cy="5" r="4.3" fill="none" stroke="#fff"/><path d="M0.7 5 H9.3 M5 0.7 V9.3" stroke="#fff"/></symbol>
    <symbol id="front-arc" viewBox="0 0 238 142"><path d="M150 4 A72 72 0 0 1 170 140 A62 62 0 0 0 150 4 Z" fill="url(#arc-fade)"/></symbol>
  </defs>
</svg>

<!-- Row 1 -->
<section class="pair" style="top:40px">
  <article class="card card--front">
    <svg class="crescent"><use href="#front-arc"/></svg>
    <div class="wordmark front__logo">Seelenklang<span class="wordmark__dot"></span></div>
    <div class="wordmark-sub front__sub">Systemanalytiker</div>
    <p class="front__services">Psycho-Kinesiologie nach Dr. Hallberg&nbsp;&nbsp;&nbsp;Neurobiologie<br>Mentalfeldtherapie&nbsp;&nbsp;&nbsp;Geistiges Familienstellen</p>
    <div class="values-band"><span>Gesundheit</span><span>Glück</span><span>Liebe</span><span>Frieden</span></div>
  </article>
  <article class="card card--back">
    <div class="back__half back__half--left">
      <div class="wordmark back__logo">Seelenklang</div>
      <div class="wordmark-sub back__logo-sub">Systemanalytiker</div>
      <div class="person-name" style="left:11px;top:57px">Udo Wendtler</div>
      <div class="person-role" style="left:11px;top:70px">Systemanalytiker</div>
      <ul class="contact" style="top:92px">
        <li><svg><use href="#icon-phone"/></svg>Schweiz</li><li class="indent">0041 790 555 214</li>
        <li><svg><use href="#icon-phone"/></svg>Deutschland</li><li class="indent">0049 170 555 48 62</li>
        <li><svg><use href="#icon-mail"/></svg>info@klarfeld-praxis.ch</li>
        <li><svg><use href="#icon-web"/></svg>www.klarfeld-praxis.ch</li>
      </ul>
    </div>
    <div class="back__half back__half--right photo" role="img" aria-label="Porträtfoto des Systemanalytikers, schwarz-weiss"></div>
    <div class="partner-badge" style="left:197px;top:102px"></div>
    <div class="partner-name" style="left:168px;top:128px">Lumen Harbor Circle</div>
    <div class="values-band"><span>Gesundheit</span><span>Glück</span><span>Liebe</span><span>Frieden</span></div>
  </article>
</section>

<!-- Row 2 -->
<section class="pair" style="top:232px">
  <article class="card card--front">
    <svg class="crescent"><use href="#front-arc"/></svg>
    <div class="wordmark front__logo">Seelenklang<span class="wordmark__dot"></span></div>
    <div class="wordmark-sub front__sub">Systemanalytiker</div>
    <div class="front__name">Udo Wendtler</div>
    <div class="values-band"><span>Gesundheit</span><span>Glück</span><span>Liebe</span><span>Frieden</span></div>
  </article>
  <article class="card card--back">
    <div class="back__half back__half--left">
      <ul class="services">
        <li>Psycho-Kinesiologie</li><li class="cont">nach Dr. Hallberg</li><li>Neurobiologie</li><li>Mentalfeldtherapie</li><li>Geistiges Familienstellen</li>
      </ul>
      <ul class="contact" style="top:90px">
        <li><svg><use href="#icon-phone"/></svg>Schweiz</li><li class="indent">0041 790 555 214</li>
        <li><svg><use href="#icon-phone"/></svg>Deutschland</li><li class="indent">0049 170 555 48 62</li>
        <li><svg><use href="#icon-mail"/></svg>info@klarfeld-praxis.ch</li>
        <li><svg><use href="#icon-web"/></svg>www.klarfeld-praxis.ch</li>
      </ul>
    </div>
    <div class="back__half back__half--right back__panel-dark">
      <svg style="position:absolute;left:0;top:0;width:119px;height:142px" viewBox="0 0 119 142"><path d="M80 64 A40 40 0 0 1 92 140 A34 34 0 0 0 80 64 Z" fill="url(#arc-fade)"/></svg>
      <div class="wordmark" style="left:6px;top:28px;font-size:17px">Seelenklang</div>
      <div class="wordmark-sub" style="left:81px;top:50px;font-size:4px">Systemanalytiker</div>
      <div class="person-name" style="left:7px;top:77px;font-style:italic">Udo Wendtler</div>
      <div class="person-role" style="left:7px;top:89px">Systemanalytiker</div>
      <div class="partner-badge" style="left:68px;top:102px"></div>
      <div class="partner-name" style="left:55px;top:124px">Lumen Harbor Circle</div>
    </div>
    <div class="values-band"><span>Gesundheit</span><span>Glück</span><span>Liebe</span><span>Frieden</span></div>
  </article>
</section>

<!-- Row 3 -->
<section class="pair" style="top:433px">
  <article class="card card--front">
    <svg class="crescent"><use href="#front-arc"/></svg>
    <div class="wordmark front__logo">Seelenklang<span class="wordmark__dot"></span></div>
    <div class="wordmark-sub front__sub">Systemanalytiker</div>
    <p class="front__services">Psycho-Kinesiologie nach Dr. Hallberg&nbsp;|&nbsp;Neurobiologie<br>Mentalfeldtherapie&nbsp;|&nbsp;Geistiges Familienstellen</p>
    <div class="values-band"><span>Gesundheit</span><span>Glück</span><span>Liebe</span><span>Frieden</span></div>
  </article>
  <article class="card card--back">
    <div class="back__half back__half--left">
      <div class="wordmark back__logo">Seelenklang</div>
      <div class="wordmark-sub back__logo-sub">Systemanalytiker</div>
      <div class="person-name" style="left:11px;top:57px">Udo Wendtler</div>
      <div class="person-role" style="left:11px;top:70px">Systemanalytiker</div>
      <ul class="contact" style="top:92px">
        <li><svg><use href="#icon-phone"/></svg>Schweiz</li><li class="indent">0041 790 555 214</li>
        <li><svg><use href="#icon-phone"/></svg>Deutschland</li><li class="indent">0049 170 555 48 62</li>
        <li><svg><use href="#icon-mail"/></svg>info@klarfeld-praxis.ch</li>
        <li><svg><use href="#icon-web"/></svg>www.klarfeld-praxis.ch</li>
      </ul>
    </div>
    <div class="back__half back__half--right photo" role="img" aria-label="Porträtfoto des Systemanalytikers, schwarz-weiss"></div>
    <div class="partner-badge" style="left:197px;top:102px"></div>
    <div class="partner-name" style="left:168px;top:128px">Lumen Harbor Circle</div>
    <div class="values-band"><span>Gesundheit</span><span>Glück</span><span>Liebe</span><span>Frieden</span></div>
  </article>
</section>

<!-- Row 4 -->
<section class="pair" style="top:625px">
  <article class="card card--front">
    <svg class="crescent"><use href="#front-arc"/></svg>
    <div class="wordmark front__logo">Seelenklang<span class="wordmark__dot"></span></div>
    <div class="wordmark-sub front__sub">Systemanalytiker</div>
    <div class="front__name">Udo Wendtler</div>
    <div class="values-band"><span>Gesundheit</span><span>Glück</span><span>Liebe</span><span>Frieden</span></div>
  </article>
  <article class="card card--back">
    <div class="back__half back__half--left">
      <ul class="services">
        <li>Psycho-Kinesiologie</li><li class="cont">nach Dr. Hallberg</li><li>Neurobiologie</li><li>Mentalfeldtherapie</li><li>Geistiges Familienstellen</li>
      </ul>
      <ul class="contact" style="top:90px">
        <li><svg><use href="#icon-phone"/></svg>Schweiz</li><li class="indent">0041 790 555 214</li>
        <li><svg><use href="#icon-phone"/></svg>Deutschland</li><li class="indent">0049 170 555 48 62</li>
        <li><svg><use href="#icon-mail"/></svg>info@klarfeld-praxis.ch</li>
        <li><svg><use href="#icon-web"/></svg>www.klarfeld-praxis.ch</li>
      </ul>
    </div>
    <div class="back__half back__half--right back__panel-dark">
      <svg style="position:absolute;left:0;top:0;width:119px;height:142px" viewBox="0 0 119 142"><path d="M80 64 A40 40 0 0 1 92 140 A34 34 0 0 0 80 64 Z" fill="url(#arc-fade)"/></svg>
      <div class="wordmark" style="left:6px;top:28px;font-size:17px">Seelenklang</div>
      <div class="wordmark-sub" style="left:81px;top:50px;font-size:4px">Systemanalytiker</div>
      <div class="person-name" style="left:7px;top:77px;font-style:italic">Udo Wendtler</div>
      <div class="person-role" style="left:7px;top:89px">Systemanalytiker</div>
      <div class="partner-badge" style="left:68px;top:102px"></div>
      <div class="partner-name" style="left:55px;top:124px">Lumen Harbor Circle</div>
    </div>
    <div class="values-band"><span>Gesundheit</span><span>Glück</span><span>Liebe</span><span>Frieden</span></div>
  </article>
</section>

<!-- Row 5 (marked) -->
<section class="pair" style="top:821px">
  <span class="reject-mark">x</span>
  <article class="card card--front">
    <svg class="crescent"><use href="#front-arc"/></svg>
    <div class="wordmark front__logo">Seelenklang<span class="wordmark__dot"></span></div>
    <div class="wordmark-sub front__sub">Systemanalytiker</div>
    <p class="front__services">Psycho-Kinesiologie nach Dr. Hallberg&nbsp;&nbsp;&nbsp;Neurobiologie<br>Mentalfeldtherapie&nbsp;&nbsp;&nbsp;Geistiges Familienstellen</p>
    <div class="values-band"><span>Gesundheit</span><span>Glück</span><span>Liebe</span><span>Frieden</span></div>
  </article>
  <article class="card card--back">
    <div class="back__half back__half--left">
      <div class="wordmark back__logo">Seelenklang</div>
      <div class="wordmark-sub back__logo-sub">Systemanalytiker</div>
      <div class="person-name" style="left:11px;top:57px">Udo Wendtler</div>
      <div class="person-role" style="left:11px;top:70px">Systemanalytiker</div>
      <ul class="contact" style="top:92px">
        <li><svg><use href="#icon-phone"/></svg>Schweiz</li><li class="indent">0041 790 555 214</li>
        <li><svg><use href="#icon-phone"/></svg>Deutschland</li><li class="indent">0049 170 555 48 62</li>
        <li><svg><use href="#icon-mail"/></svg>info@klarfeld-praxis.ch</li>
        <li><svg><use href="#icon-web"/></svg>www.klarfeld-praxis.ch</li>
      </ul>
    </div>
    <div class="back__half back__half--right photo" role="img" aria-label="Porträtfoto des Systemanalytikers, schwarz-weiss"></div>
    <div class="partner-badge" style="left:197px;top:102px"></div>
    <div class="partner-name" style="left:168px;top:128px">Lumen Harbor Circle</div>
    <div class="values-band"><span>Gesundheit</span><span>Glück</span><span>Liebe</span><span>Frieden</span></div>
  </article>
</section>

<!-- Row 6 (marked) -->
<section class="pair" style="top:1014px">
  <span class="reject-mark">x</span>
  <article class="card card--front">
    <svg class="crescent"><use href="#front-arc"/></svg>
    <div class="wordmark front__logo">Seelenklang<span class="wordmark__dot"></span></div>
    <div class="wordmark-sub front__sub">Systemanalytiker</div>
    <div class="front__name">Udo Wendtler</div>
    <div class="values-band"><span>Gesundheit</span><span>Glück</span><span>Liebe</span><span>Frieden</span></div>
  </article>
  <article class="card card--back">
    <div class="back__half back__half--left">
      <ul class="services">
        <li>Psycho-Kinesiologie</li><li class="cont">nach Dr. Hallberg</li><li>Neurobiologie</li><li>Mentalfeldtherapie</li><li>Geistiges Familienstellen</li>
      </ul>
      <ul class="contact" style="top:90px">
        <li><svg><use href="#icon-phone"/></svg>Schweiz</li><li class="indent">0041 790 555 214</li>
        <li><svg><use href="#icon-phone"/></svg>Deutschland</li><li class="indent">0049 170 555 48 62</li>
        <li><svg><use href="#icon-mail"/></svg>info@klarfeld-praxis.ch</li>
        <li><svg><use href="#icon-web"/></svg>www.klarfeld-praxis.ch</li>
      </ul>
    </div>
    <div class="back__half back__half--right back__panel-dark">
      <svg style="position:absolute;left:0;top:0;width:119px;height:142px" viewBox="0 0 119 142"><path d="M80 64 A40 40 0 0 1 92 140 A34 34 0 0 0 80 64 Z" fill="url(#arc-fade)"/></svg>
      <div class="wordmark" style="left:6px;top:28px;font-size:17px">Seelenklang</div>
      <div class="wordmark-sub" style="left:81px;top:50px;font-size:4px">Systemanalytiker</div>
      <div class="person-name" style="left:7px;top:77px;font-style:italic">Udo Wendtler</div>
      <div class="person-role" style="left:7px;top:89px">Systemanalytiker</div>
      <div class="partner-badge" style="left:68px;top:102px"></div>
      <div class="partner-name" style="left:55px;top:124px">Lumen Harbor Circle</div>
    </div>
    <div class="values-band"><span>Gesundheit</span><span>Glück</span><span>Liebe</span><span>Frieden</span></div>
  </article>
</section>

</body>
</html>
```